I need a business card for myself, being a proprietor of a funeral parlor based in Manila. I'd like the card to have either of the following:
White Font on Black Background
or
Black Font on White Background
No logo is needed however I will appreciate any efforts to show a symbol of eternal happiness, aptly designed with above mentioned colors in mind.
Company name, address and contact on the lower right corner.
Logo or symbol anywhere.
Quillstone Funeral Services
+639174826351
darvik4521@pelmora.com
corner of Brisco Avenue and Velhurst Street
Makati City, Philippines
Thank you.
Update: Please include a small dove in your design. You are free to choose where you would like it on the card.

```html
<!DOCTYPE html>
<html lang="en">
<head>
<meta charset="utf-8">
<title>Quillstone Funeral Services – Business Card</title>
<link rel="stylesheet" href="https://fonts.googleapis.com/css2?family=Ubuntu:wght@400;700&display=swap">
<style>
  :root {
    --stage: #8a929a;
    --card-red: #b81f18;
    --card-black: #000000;
    --knot-red: #d12a22;
    --dove-dark: #111111;
    --text-white: #ffffff;
  }
  * { margin: 0; padding: 0; box-sizing: border-box; }
  html, body {
    width: 1200px;
    height: 1000px;
    overflow: hidden;
    background: var(--stage);
  }
  .canvas {
    width: 1200px;
    height: 1000px;
    display: flex;
    align-items: center;
    justify-content: center;
  }
  .business-card {
    width: 1000px;
    height: 572px;
    display: flex;
    box-shadow: 0 10px 30px rgba(0,0,0,0.35);
    font-family: "Ubuntu", sans-serif;
  }
  .symbol-panel {
    width: 370px;
    background: var(--card-black);
    display: flex;
    align-items: center;
    justify-content: center;
  }
  .eternal-knot-area {
    width: 180px;
    height: 180px;
    border-radius: 40px;
    background: radial-gradient(circle, var(--knot-red) 0%, #7a1510 100%);
    transform: rotate(45deg);
  }
  .info-panel {
    flex: 1;
    background: var(--card-red);
    color: var(--text-white);
    display: flex;
    flex-direction: column;
    align-items: center;
    padding-top: 120px;
  }
  .dove-area {
    width: 130px;
    height: 70px;
    border-radius: 50% 50% 45% 45%;
    background: var(--dove-dark);
    margin-bottom: 34px;
  }
  .company-name {
    font-weight: 700;
    font-size: 38px;
    letter-spacing: 0.3px;
    margin-bottom: 56px;
  }
  .contact-details {
    font-weight: 400;
    font-size: 24px;
    line-height: 1.45;
    text-align: center;
  }
  .contact-details .divider {
    display: inline-block;
    width: 4px;
    height: 20px;
    background: var(--text-white);
    margin: 0 8px;
    vertical-align: -2px;
  }
</style>
</head>
<body>
  <main class="canvas">
    <article class="business-card">
      <section class="symbol-panel">
        <div class="eternal-knot-area" role="img" aria-label="Red endless knot, symbol of eternal happiness"></div>
      </section>
      <section class="info-panel">
        <div class="dove-area" role="img" aria-label="Small black dove in flight with a white outline"></div>
        <h1 class="company-name">Quillstone Funeral Services</h1>
        <address class="contact-details">
          <p>E : darvik4521@pelmora.com<span class="divider"></span>P : +639174826351</p>
          <p>corner of Brisco Avenue and Velhurst Street</p>
          <p>Makati City, Philippines</p>
        </address>
      </section>
    </article>
  </main>
</body>
</html>
```